Corporate flyer introducing a brand new technology apprenticeship program in Australia!

A professional, yet clean and contemporary looking flyer to advertise a brand new service offering in a simple, easy to read format with engaging images. Here is a link to our current online brochure which outlines the program we would like to advertise in a hardcopy flyer/brochure format: https://pages.vendrap.com/Information-on-Technology-Higher-Apprenticeships-for-Employers-Victoria-kT3pzqW7LmRe

Target Market(s)

Medium to large sized businesses involved in using cutting edge technology, such as engineering and advanced manufracturing (3D printing etc)

Industry/Entity Type

Engineering

Colors

Designer to choose colors to be used in the design.

Requirements
Must have
• Contemporary, clean looking, easy to read, tech/engineering/advanced manufacturing related imagery
Nice to have
• Some ideas about different sizes/styles (eg something other than a plain A4 sheet)
Should not have
• Unprofessional or offensive language

```html
<!DOCTYPE html>
<html lang="en">
<head>
<meta charset="utf-8">
<title>Technology Higher Apprentices – Brochure</title>
<link href="https://fonts.googleapis.com/css2?family=Montserrat:wght@400;600;700&family=Open+Sans:wght@400;600;700&display=swap" rel="stylesheet">
<style>
:root{
  --orange:#e8572a;
  --slate:#37434b;
  --blue:#2a7dc0;
  --row:#dfe2e5;
  --stage:#8f969c;
  --ink:#2b2f33;
  --white:#ffffff;
}
*{box-sizing:border-box;margin:0;padding:0}
html,body{width:1200px;height:2486px;overflow:hidden}
body{background:var(--stage);font-family:"Open Sans",Arial,sans-serif;color:var(--ink);position:relative}
.spread{position:absolute;left:36px;width:1128px;height:775px;background:var(--white);box-shadow:0 4px 14px rgba(0,0,0,.25);overflow:hidden}
.cover-pair{position:absolute;left:224px;top:40px;width:752px;height:775px;overflow:hidden;box-shadow:0 4px 14px rgba(0,0,0,.25)}
.cover-pair .spread{left:-376px;top:0;box-shadow:none}
.outside-a{top:850px}
.inside{top:1650px}
.shapes{position:absolute;left:0;top:0}
.photo{position:absolute}
.photo-workshop{left:0;top:0;width:376px;height:175px;background:linear-gradient(135deg,#6d7a84,#b9c0c4 45%,#4d5961)}
.photo-laptop{left:605px;top:120px;width:330px;height:330px;border-radius:50%;border:6px solid var(--white);background:radial-gradient(circle at 55% 45%,#d8d2c6,#9c8d72 55%,#4e5a3e)}
.panel{position:absolute;top:0;width:376px;height:775px}
.p1{left:0}.p2{left:376px}.p3{left:752px}
/* outside panel 1 */
.program-intro{position:absolute;left:20px;top:192px;width:336px;color:var(--white)}
.program-intro h2{font-family:"Montserrat",sans-serif;font-size:15px;font-weight:700;letter-spacing:.3px}
.program-intro h2 span{color:var(--orange)}
.program-intro h3{font-family:"Montserrat",sans-serif;font-size:11.5px;font-weight:400;margin:3px 0 16px}
.program-intro p{font-size:9.4px;line-height:1.5;margin-bottom:10px}
.why{position:absolute;left:18px;top:526px;width:342px;bottom:10px;overflow:hidden}
.why h2{font-family:"Montserrat",sans-serif;font-size:14px;font-weight:700;color:var(--orange);border-bottom:2px solid var(--ink);padding-bottom:3px;margin-bottom:6px}
.why h2 span{color:var(--ink)}
.why p{font-size:6.6px;line-height:1.3;margin-bottom:4px}
/* outside panel 2 */
.move-forward{position:absolute;left:0;top:14px;width:376px;text-align:center;color:var(--white)}
.move-forward h2{font-family:"Montserrat",sans-serif;font-size:23px;font-weight:400;letter-spacing:.5px}
.move-forward .lead{font-size:11px;margin:2px 0 14px}
.move-forward p{font-size:10px;line-height:1.45;padding:0 24px}
.contact{position:absolute;left:40px;top:222px;width:180px;text-align:center;color:var(--white);font-size:12.5px;font-weight:600}
.contact .icon{width:32px;height:32px;border-radius:50%;background:var(--orange);margin:0 auto 6px;display:flex;align-items:center;justify-content:center}
.contact .item{margin-bottom:22px}
.socials{display:flex;justify-content:center;gap:7px}
.socials span{width:20px;height:20px;border-radius:50%;background:var(--blue);display:block}
.brand{display:flex;align-items:center;gap:10px;font-family:"Montserrat",sans-serif;font-weight:700;color:var(--slate);font-size:24px;letter-spacing:.5px}
.brand i{width:22px;height:22px;background:var(--orange);display:block}
.brand-back{position:absolute;left:0;width:376px;top:585px;justify-content:center}
.brand-cover{position:absolute;left:0;width:376px;top:66px;justify-content:center}
.web-bar{position:absolute;height:40px;line-height:40px;text-align:center;color:var(--white);font-size:13px;letter-spacing:.5px}
.web-back{left:24px;width:330px;top:705px;background:var(--orange)}
.web-cover{left:18px;width:340px;top:705px;background:var(--slate)}
.cover-title{position:absolute;left:0;top:548px;width:376px;text-align:center;color:var(--white);font-family:"Montserrat",sans-serif;font-weight:700;font-size:32px;line-height:1.12}
/* inside */
.inside .panel{padding:18px 20px}
.inside h2{font-family:"Montserrat",sans-serif;font-size:15px;font-weight:700;color:var(--ink);margin-bottom:8px}
.inside h2 span{color:var(--orange)}
.inside p{font-size:9.2px;line-height:1.45;margin-bottom:8px}
.units{margin-top:4px}
.units-table{width:300px;margin:0 auto 12px;border:1px solid #c9cdd0;font-size:8.6px;text-align:center}
.units-table .head{background:var(--blue);color:var(--white);font-weight:700;font-size:11px;height:22px;line-height:22px;border-radius:6px 6px 0 0}
.units-table li{list-style:none;height:13.6px;line-height:13.6px;white-space:nowrap;overflow:hidden}
.units-table li:nth-child(even){background:var(--row)}
.industry{background:var(--orange);color:var(--white)}
.industry h2{color:var(--white)}
.industry h2 span{color:var(--slate)}
.industry p{color:var(--white)}
.diagram{width:336px;height:78px;margin:6px 0 14px;background:linear-gradient(90deg,#cfe3ef,#e9f2f7 50%,#cfe3ef)}
.intake .story{border:1px solid var(--ink);padding:14px 10px 6px;margin:18px 0 8px;position:relative}
.intake .story h3{position:absolute;top:-9px;left:8px;background:var(--white);padding:0 5px;font-family:"Montserrat",sans-serif;font-size:12px;font-weight:700;color:var(--ink)}
.intake .story h3 span{color:var(--orange)}
.intake .story p{font-size:8.8px}
</style>
</head>
<body>

<div class="cover-pair">
  <section class="spread">
    <svg class="shapes" width="1128" height="775" viewBox="0 0 1128 775">
      <rect x="376" y="0" width="376" height="160" fill="var(--orange)"/>
      <path d="M376 160 H500 A170 170 0 0 1 500 500 H376 Z" fill="var(--slate)"/>
      <rect x="752" y="515" width="376" height="260" fill="var(--orange)"/>
    </svg>
    <div class="photo photo-laptop" role="img" aria-label="Photo of hands working on a laptop at an outdoor table"></div>
    <div class="panel p2">
      <div class="move-forward">
        <h2>LET'S MOVE FORWARD</h2>
        <div class="lead">The future is determined by the decisions you make today.</div>
        <p>Lay a strong foundation for the future success of your business by talking to us about Higher Apprenticeships today.</p>
      </div>
      <div class="contact">
        <div class="item"><div class="icon"><svg width="16" height="16" viewBox="0 0 24 24"><path fill="#fff" d="M6.6 10.8a15 15 0 0 0 6.6 6.6l2.2-2.2c.3-.3.7-.4 1-.2 1.1.4 2.3.6 3.6.6.6 0 1 .4 1 1V20c0 .6-.4 1-1 1A17 17 0 0 1 3 4c0-.6.4-1 1-1h3.5c.6 0 1 .4 1 1 0 1.3.2 2.5.6 3.6.1.3 0 .7-.2 1z"/></svg></div>1300 555 019</div>
        <div class="item"><div class="icon"><svg width="16" height="16" viewBox="0 0 24 24"><path fill="#fff" d="M3 5h18v14H3z"/><path d="M3 6l9 7 9-7" fill="none" stroke="#e8572a" stroke-width="2"/></svg></div>talent@vantorgroup.com.au</div>
        <div class="socials"><span></span><span></span><span></span><span></span></div>
      </div>
      <div class="brand brand-back"><i></i>VANTOR GROUP</div>
      <div class="web-bar web-back">www.vantorgroup.com.au</div>
    </div>
    <div class="panel p3">
      <div class="brand brand-cover"><i></i>VANTOR GROUP</div>
      <div class="cover-title">TECHNOLOGY<br>HIGHER<br>APPRENTICES</div>
      <div class="web-bar web-cover">www.vantorgroup.com.au</div>
    </div>
  </section>
</div>

<section class="spread outside-a">
  <svg class="shapes" width="1128" height="775" viewBox="0 0 1128 775">
    <rect x="0" y="175" width="376" height="345" fill="var(--slate)"/>
    <rect x="376" y="0" width="376" height="160" fill="var(--orange)"/>
    <path d="M376 160 H500 A170 170 0 0 1 500 500 H376 Z" fill="var(--slate)"/>
    <rect x="752" y="515" width="376" height="260" fill="var(--orange)"/>
  </svg>
  <div class="photo photo-workshop" role="img" aria-label="Photo of apprentices building equipment in a workshop"></div>
  <div class="photo photo-laptop" role="img" aria-label="Photo of hands working on a laptop at an outdoor table"></div>

  <div class="panel p1">
    <div class="program-intro">
      <h2>VANTOR GROUP <span>TALENT SOLUTIONS</span></h2>
      <h3>TECHNOLOGY HIGHER APPRENTICES PROGRAM</h3>
      <p>Join industry leaders in this unique program aimed at future proofing Australian businesses.</p>
      <p>The Technology Higher Apprenticeships combine the best of Higher Education and Vocational learning models by training future technicians to a higher skill and knowledge level to meet the needs of an Industry 4.0 based economy.</p>
      <p>These Higher Apprentices are employed in a model similar to a traditional paid apprenticeship while they are also enrolled in a Diploma of Applied Technologies, followed by an Associate Degree covering a range of topics related to emerging technology. The Higher Apprentices will also complete a number of intensive projects where they will commission a cyber-physical system to provide a solution or enhancement for your business. During these projects, the Higher Apprentices will have access to Kelmont's world-class Factory of the Future.</p>
    </div>
    <div class="why">
      <h2>WHY <span>THIS MODEL?</span></h2>
      <p>The world of work is changing. The Australian economy is not only moving to a more knowledge-based economy but one that requires a higher and more pervasive level of digital skills as well. Accordingly, the Australian workforce needs to be more highly skilled than ever.</p>
      <p>The traditional Certificate III trade qualification will continue to meet the needs of a broad range of occupations, but the emerging occupations are ones that require higher skills in areas such as creativity, problem solving, advanced reasoning, and complex judgement. ABS data is showing that the Australian economy is reflecting continued growth in the demand for highly skilled workers and slower or no growth for lower-skilled workers.</p>
      <p>Universities have always provided the opportunities for the development of high level skills, with their focus on bachelor degrees and higher, but not all of the emerging demand is for workers at this level. Much of the demand will be for workers who can combine vocational skills with higher level technical and enterprise skills. Think Diplomas, Advanced Diplomas and Associate Degrees. The apprenticeship model is well placed as the means to meet this demand.</p>
      <p>The Technology Higher Apprenticeships program aims to equip these future workers with the practical and knowledge-based capabilities to assist industry take the required steps to stay at the forefront of Engineering, manufacturing and technology and move forward into the Industry 4.0 economy.</p>
    </div>
  </div>

  <div class="panel p2">
    <div class="move-forward">
      <h2>LET'S MOVE FORWARD</h2>
      <div class="lead">The future is determined by the decisions you make today.</div>
      <p>Lay a strong foundation for the future success of your business by talking to us about Higher Apprenticeships today.</p>
    </div>
    <div class="contact">
      <div class="item"><div class="icon"><svg width="16" height="16" viewBox="0 0 24 24"><path fill="#fff" d="M6.6 10.8a15 15 0 0 0 6.6 6.6l2.2-2.2c.3-.3.7-.4 1-.2 1.1.4 2.3.6 3.6.6.6 0 1 .4 1 1V20c0 .6-.4 1-1 1A17 17 0 0 1 3 4c0-.6.4-1 1-1h3.5c.6 0 1 .4 1 1 0 1.3.2 2.5.6 3.6.1.3 0 .7-.2 1z"/></svg></div>1300 555 019</div>
      <div class="item"><div class="icon"><svg width="16" height="16" viewBox="0 0 24 24"><path fill="#fff" d="M3 5h18v14H3z"/><path d="M3 6l9 7 9-7" fill="none" stroke="#e8572a" stroke-width="2"/></svg></div>talent@vantorgroup.com.au</div>
      <div class="socials"><span></span><span></span><span></span><span></span></div>
    </div>
    <div class="brand brand-back"><i></i>VANTOR GROUP</div>
    <div class="web-bar web-back">www.vantorgroup.com.au</div>
  </div>

  <div class="panel p3">
    <div class="brand brand-cover"><i></i>VANTOR GROUP</div>
    <div class="cover-title">TECHNOLOGY<br>HIGHER<br>APPRENTICES</div>
    <div class="web-bar web-cover">www.vantorgroup.com.au</div>
  </div>
</section>

<section class="spread inside">
  <div class="panel p1 course">
    <h2><span>COURSE</span> STRUCTURE</h2>
    <p>The Program currently has a 4-year delivery timeline. Vantor Group Talent Solutions envisages working with each company hosting a Technology Higher Apprentice, as well as with the relevant training provider on appropriate attendance schedules that maximise benefits for students, and the workplace. Training will be conducted in the work place, as well as the off-the-job delivery at the relevant training provider's facilities.</p>
    <p>The following is an indication of the current units of study for the Victorian Program which is currently being delivered by Kelmont University of Technology's Vocational and Higher Educational sectors.</p>
    <h2 class="units"><span>UNITS</span> OF STUDY</h2>
    <ul class="units-table">
      <div class="head">Years 1 and 2: Diploma Level</div>
      <li>Working in Industry 4.0</li>
      <li>Use hand and power tools</li>
      <li>Perform Computations</li>
      <li>Apply principles of OHS in the work environment</li>
      <li>Analyse a simple electrical system circuit</li>
      <li>Produce components using CAD and CAM technologies</li>
      <li>Implement and problem solve a PLC-based control system</li>
      <li>Troubleshoot digital control systems</li>
      <li>Apply project life cycle management processes</li>
      <li>Produce and manage technical documentation</li>
      <li>Use SCADA system to monitor and control a process</li>
      <li>Apply principles of networking for manufacturing</li>
      <li>Analyse and manage Big Data in cloud-based systems</li>
      <li>Work safely with collaborative robots</li>
      <li>Project: Commission a cyber-physical system</li>
      <li>Apply principles of sensors and instrumentation</li>
    </ul>
    <ul class="units-table">
      <div class="head">Years 3 and 4: Associate Degree Level</div>
      <li>Working in Industry 4.0</li>
      <li>Engineering skills for Industry 4.0</li>
      <li>CAD / CAM and engineering materials</li>
      <li>Industrial networking and cloud computing</li>
      <li>Electrical systems</li>
      <li>Object oriented programming for industrial control</li>
      <li>Digital control systems</li>
      <li>Cyber physical system integration (Major Project)</li>
      <li>Software tools for Industry 4.0</li>
      <li>Advanced digital control systems</li>
      <li>Advanced electrical machines</li>
      <li>Predictive engineering analytics</li>
      <li>Robotics and digital twin</li>
      <li>Cyber security and cloud services</li>
      <li>Distributed control in a smart factory</li>
      <li>Smart product design using Industry 4.0</li>
      <li>Industry placement and reflection</li>
    </ul>
  </div>

  <div class="panel p2 industry">
    <h2>WHAT IS <span>INDUSTRY 4.0</span></h2>
    <p>The term Industry 4.0 encompasses the digitalisation of production processes based on devices autonomously communicating with each other along a value chain. Production units become 'smart factories' where computer-driven systems monitor physical processes.</p>
    <p>Automation, sensors, cloud computing, big data analytics and machine-to-machine communication are driving new business opportunities through integration with the global supply chain. Industry 4.0 technologies make it possible to gather and analyse data across machines enabling faster, more flexible, and more efficient processes to produce higher quality goods at reduced costs.</p>
    <p>This in turn increases manufacturing productivity, shifts economics, fosters industrial growth, modifies the profile of the workforce and ultimately changes the competitiveness of companies.</p>
    <p>What does this mean for Australian businesses? Essentially it requires businesses to innovate, collaborate and redefine future parameters. Whilst innovation doesn't necessarily transform an industry overnight, failure to build capability and develop forward thinking infrastructure has the potential to lead to irrelevance much quicker than expected.</p>
    <div class="diagram" role="img" aria-label="Illustration of the four industrial revolutions from steam power to smart factories"></div>
    <h2>INDUSTRY 4.0 <span>HIGHER APPRENTICESHIPS PILOT PROGRAM</span></h2>
    <p>The program utilises an apprenticeship framework to deliver a new Diploma and Associate Degree in Applied Technologies.</p>
    <p>The original project is funded as a pilot by the Australian Government, led and managed by Vantor Group, and implemented in collaboration with Arvion Systems and Kelmont University of Technology.</p>
    <p>Focusing on Industry 4.0 and the Internet of Things, IT Disruptive Technologies, Engineering, Design and Business, the course will enable employers to train future technicians with a higher skills level to meet their needs in an Industry 4.0 based economy.</p>
    <p>The pilot combines the best of university and vocational learning models to improve Science, Technology, Engineering and Math (STEM) skills of technically minded participants, incorporating skills for business and design.</p>
    <p>The hands on and worked based component ensures apprentices are productive in Industry whilst applying the advanced knowledge gained from the off-the-job training.</p>
  </div>

  <div class="panel p3 intake">
    <h2><span>CURRENT</span> INTAKE</h2>
    <p>Vantor Group Talent Solutions has a current 2018 intake of Higher Apprentices who are working towards an Associate Degree in Applied Technologies and working within Vantor Group member companies, experiencing both on and off-the-job training like never before.</p>
    <p>Here are some examples of their learnings and contributions to date:</p>
    <div class="story">
      <h3><span>STORY 1:</span> OUT OF THE CLOSET</h3>
      <p>One of the companies had a $60,000 thermal imaging camera sitting in the cupboard collecting dust because they had no time or resources to dedicate towards investigating how to use and calibrate this technology and its software, (which is a rather complex and time consuming process). The Higher Apprentice was given this camera by his Supervisor and told to figure out how to use it with the view to eventually training the senior staff. The Higher Apprentice was also learning about this type of technology as part of his formal qualification. The Higher Apprentice dedicated the next few weeks to learning about this specific camera and was able to provide significant learnings to the business about calibration and use.</p>
      <p>The benefits of knowing how to use this technology will be enormous as the company can use the camera to monitor heat levels of each layer during the 3D printing process which will produce 'real time' data on heat stress, as opposed to the current practice of X-Ray / thermal scanning of welded products. Therefore, the program will provide efficiencies and a return on investment for the camera, as well as saving time in training staff to use the technology.</p>
    </div>
    <div class="story">
      <h3><span>STORY 2:</span> THE MISSING LINK</h3>
      <p>One of the Industry 4.0 Higher Apprentices saved a company $6,000 by identifying a way to re-purpose a robotic welding nozzle that could replace the current faulty nozzle. The company had placed an order for several new components which would have cost them approximately $6,000.</p>
      <p>This is an ideal example of how Higher Apprenticeships combine technology and practical skills as this Higher Apprentice incorporates use of CAD drawings and looks at the actual machine and identified some missing links. This skill is critical because too often there is a disconnect between what the technical staff are able to articulate in drawings and what the production staff can actually make.</p>
    </div>
    <div class="story">
      <h3><span>STORY 3:</span> PICTURE PERFECT</h3>
      <p>One of the Industry 4.0 Higher Apprentices was asked to come up with CAD drawings of a very large and complex piece of machinery. He produced moving drawings to such a high level that, once completed, they could even be used to train people on how to operate the complex machine before they've even seen or touched it.</p>
    </div>
  </div>
</section>

</body>
</html>
```